Net Clarity Partners Needs a New Business Card Design

Attached is my new logo that ArtFolkHub created and picture of me for the back of the business card. Also attached is the information to include on the business card (on my existing business card design - QZR4 file attached).

The designer also provided a treatment of my logo that I really like if you can use it somehow. Also attached - file name "Preferred Version of New Logo."

Maren Falstead

Net Clarity Partners
4517 Pellam Rd., #349
Houston, TX 77348

Tel: (832) 555-0147
www.netclaritypartners.example
maren@netclaritypartners.example

Thank you.

Reason: I'm close but am having a hard time deciding.

Target Market(s)

attorneys and law firms

Industry/Entity Type

Legal

Contact Information for Business Card

Proved in the Project Description

Font styles to use
Other font styles liked:
• I am open on font - no script though.

Colors
2d73b3
33a6d7

Requirements
Must have
• my logo
• company name & contact info
• my picture on the back
• colors that coordinate with the logo
Nice to have
• love to use the treated version of the logo if possible

```html
<!DOCTYPE html>
<html lang="en">
<head>
<meta charset="utf-8">
<title>Net Clarity Partners – Business Card</title>
<link rel="stylesheet" href="https://fonts.googleapis.com/css2?family=Open+Sans:wght@400;600;700&display=swap">
<style>
  :root {
    --sky: #08a9e2;
    --grey: #8e9195;
    --grey-light: #b8bbbf;
    --ink: #1a1a1a;
    --paper: #ffffff;
    --stage: #3a3b3d;
  }
  * { box-sizing: border-box; margin: 0; padding: 0; }
  html, body { width: 1200px; height: 900px; overflow: hidden; }
  body {
    background: var(--stage);
    font-family: "Open Sans", Arial, sans-serif;
    display: flex; flex-direction: column; align-items: center; justify-content: center;
    gap: 50px;
  }
  .card {
    position: relative;
    width: 600px; height: 343px;
    overflow: hidden;
    box-shadow: 0 10px 28px rgba(0,0,0,.45);
  }

  /* ---------- brand lockup ---------- */
  .brand { display: flex; flex-direction: column; gap: 5px; }
  .brand-name {
    display: flex; align-items: center; gap: 9px;
    font-weight: 700; text-transform: uppercase; line-height: 1; white-space: nowrap;
  }
  .brand-mark { background: currentColor; flex: none; }
  .tagline { font-weight: 600; text-transform: uppercase; white-space: nowrap; }

  /* ---------- back ---------- */
  .card-back { background: var(--sky); }
  .card-back .brand { position: absolute; left: 44px; top: 84px; color: var(--paper); }
  .card-back .brand-name { font-size: 22px; letter-spacing: .4px; }
  .card-back .brand-mark { width: 18px; height: 18px; }
  .card-back .tagline { color: var(--paper); font-size: 9px; letter-spacing: 2.8px; padding-left: 27px; }
  .card-back .site {
    position: absolute; left: 44px; top: 166px;
    color: var(--paper); font-size: 14px; letter-spacing: .6px;
  }
  .portrait {
    position: absolute; right: 30px; bottom: 0;
    width: 200px; height: 262px;
    border-radius: 100px 100px 0 0;
    background: linear-gradient(180deg, #c9a77a 0%, #e6bfa4 42%, #d7a88f 58%, #3c43b8 78%, #2f35a0 100%);
  }

  /* ---------- front ---------- */
  .card-front { background: var(--paper); }
  .card-front .brand { position: absolute; left: 0; right: 0; top: 58px; align-items: center; color: var(--sky); }
  .card-front .brand-name { font-size: 26px; letter-spacing: .5px; }
  .card-front .brand-mark { width: 22px; height: 22px; }
  .card-front .tagline { color: var(--grey); font-size: 10px; letter-spacing: 4px; }
  .rule {
    position: absolute; left: 40px; right: 40px; top: 142px;
    height: 1.5px; background: var(--grey);
  }
  .contact {
    position: absolute; left: 40px; top: 170px;
    list-style: none; font-size: 15px; color: var(--ink); line-height: 1.45;
  }
  .contact li { display: flex; align-items: center; gap: 9px; }
  .contact svg { width: 13px; height: 13px; fill: var(--sky); flex: none; }
  .person { position: absolute; right: 40px; top: 166px; text-align: right; }
  .person-name {
    display: inline-block; color: var(--sky); font-size: 25px; font-weight: 400;
    padding-bottom: 2px; border-bottom: 1.5px solid var(--grey);
  }
  .address { margin-top: 10px; font-size: 16px; color: var(--ink); line-height: 1.3; }
  .sweep { position: absolute; left: 0; bottom: 0; width: 600px; height: 120px; }
  .front-site {
    position: absolute; right: 40px; bottom: 10px;
    color: var(--paper); font-size: 16px; letter-spacing: .4px;
  }
</style>
</head>
<body>

  <section class="card card-back" aria-label="Business card back">
    <div class="brand">
      <div class="brand-name"><span class="brand-mark"></span>Net Clarity Partners</div>
      <div class="tagline">Smart Marketing for Law Firms</div>
    </div>
    <p class="site">www.netclaritypartners.example</p>
    <div class="portrait" role="img" aria-label="Portrait photo of Maren Falstead"></div>
  </section>

  <section class="card card-front" aria-label="Business card front">
    <div class="brand">
      <div class="brand-name"><span class="brand-mark"></span>Net Clarity Partners</div>
      <div class="tagline">Smart Marketing for Law Firms</div>
    </div>
    <div class="rule"></div>

    <ul class="contact">
      <li>
        <svg viewBox="0 0 24 24" aria-hidden="true"><path d="M6.6 10.8a15.1 15.1 0 0 0 6.6 6.6l2.2-2.2a1 1 0 0 1 1-.25 11.4 11.4 0 0 0 3.6.57 1 1 0 0 1 1 1V20a1 1 0 0 1-1 1A17 17 0 0 1 3 4a1 1 0 0 1 1-1h3.5a1 1 0 0 1 1 1c0 1.25.2 2.45.57 3.57a1 1 0 0 1-.25 1z"/></svg>
        (832) 555-0147
      </li>
      <li>
        <svg viewBox="0 0 24 24" aria-hidden="true"><path d="M2 5h20v14H2z M2 5l10 8 10-8" stroke="#fff" stroke-width="1.6"/></svg>
        maren@netclaritypartners.example
      </li>
    </ul>

    <div class="person">
      <h1 class="person-name">Maren Falstead</h1>
      <p class="address">4517 Pellam Rd., #349<br>Houston, TX 77348</p>
    </div>

    <svg class="sweep" viewBox="0 0 600 120" preserveAspectRatio="none" aria-hidden="true">
      <path d="M0 20 C150 40 300 75 420 120 L0 120 Z" fill="var(--grey-light)"/>
      <path d="M0 34 C140 52 260 80 360 120 L0 120 Z" fill="var(--paper)"/>
      <path d="M0 50 C120 64 230 84 300 92 L600 82 L600 120 L0 120 Z" fill="var(--sky)"/>
      <path d="M0 44 C140 58 240 78 310 90" fill="none" stroke="var(--grey)" stroke-width="2"/>
    </svg>
    <p class="front-site">www.netclaritypartners.example</p>
  </section>

</body>
</html>
```